Tour operator needs simple coded WordPress site (updated extra payment for coding and guaranteed)

[update 9/7/2015]
If you design a new logo and it gets accepted, even if we use another template with your logo you will get $50
[update 8/7/2015]
Update on questions about dual-language
For dual languages we are happy to set up a second site with the same designs in a second language.
For the design aspect just allow the user to switch between languages with an icon.
For the coding, a replica of the site on a second server will do (to save messing around with multiple language plugins) - we will populate it with Chinese text
[original post]
Simple coded WordPress site for tours
You can choose to design only or design and code ($340 design, $150 bonus for coding)
Open design brief - use your creativity
Will be in 2 languages (English and Chinese) but design needs only to be in one language
Winning design will be chosen only from home page, but the winner must make a second standard template page when chosen at no extra cost.
Must be responsive design
We only need homepage and standard template page design and coding, we will populate the pages
You can use design ideas from our pamphlet if you like - attached
Only a sample logo and colors on website and pamphlet - feel free to change as the current ones seem restrictive
Current website framework only to give an idea of the number of pages and basic menu structure (no need to use existing navigation style or any style at all for that matter, open brief)
http://brightwaterlearningtrips.com.au/
Target Market(s)
Chinese parents of kids 10-14 (the kids will take the tour)
Industry/Entity Type
Tour
Number of Pages Required
2 page
Look and feel
Each slider illustrates characteristics of the customer's brand and the style your logo design should communicate.

```html
<!DOCTYPE html>
<html lang="en">
<head>
<meta charset="utf-8">
<title>Brightwater Learning Trips</title>
<link href="https://fonts.googleapis.com/css2?family=Open+Sans:wght@400;600;700&display=swap" rel="stylesheet">
<style>
:root{
  --orange:#f5a21c;
  --orange-dark:#e58e0c;
  --blue:#1d8fd6;
  --navy:#1e4f8c;
  --cyan:#27b6e0;
  --cyan-light:#7fd6f0;
  --green:#6fb43f;
  --text:#6d6d6d;
  --muted:#9a9a9a;
  --line:#e3e3e3;
  --page:#ffffff;
  --footer:#f1f1f1;
}
*{margin:0;padding:0;box-sizing:border-box}
html,body{width:847px;height:1200px;overflow:hidden;background:var(--page)}
body{font-family:'Open Sans',Arial,sans-serif;color:var(--text);position:relative}
.wrap{position:absolute;left:127px;width:593px}

.site-header{position:absolute;top:0;left:0;width:847px;height:50px;background:#fff}
.brand{position:absolute;left:127px;top:13px;display:flex;align-items:center;gap:7px}
.brand-mark{width:14px;height:14px;border-radius:50%;background:var(--navy)}
.brand-name{font-size:15px;font-weight:700;color:var(--navy)}
.lang{position:absolute;right:127px;top:16px;display:flex;align-items:center;gap:4px;border:1px solid var(--line);padding:2px 5px;font-size:8px;color:#666}
.lang-flag{width:11px;height:7px;background:var(--navy)}
.lang svg{width:6px;height:4px}

.main-nav{position:absolute;top:50px;left:0;width:847px;height:26px;background:linear-gradient(var(--orange),var(--orange-dark))}
.main-nav ul{list-style:none;display:flex;justify-content:center;gap:0;height:100%}
.main-nav li{color:#fff;font-size:8px;font-weight:600;letter-spacing:.5px;padding:0 18px;line-height:26px;border-right:1px solid rgba(255,255,255,.35)}
.main-nav li:last-child{border-right:0}

.hero{position:absolute;top:76px;left:0;width:847px;height:192px;background:linear-gradient(180deg,#8fc9ec 0%,#cde7f6 60%,#e9f2f2 100%)}
.hero-photo{position:absolute;right:100px;top:0;width:420px;height:192px;background:linear-gradient(90deg,rgba(200,225,240,0) 0%,#b9a88f 45%,#e6d6c4 70%,#d9c1a6 100%)}
.hero-copy{position:absolute;left:127px;top:36px;width:250px}
.hero-kicker{font-size:12px;color:var(--orange);font-weight:600}
.hero-title{font-size:30px;color:var(--navy);font-weight:700;line-height:1.15;margin-top:2px}
.hero-text{font-size:7px;color:#4d6f8c;line-height:1.5;margin-top:6px}
.dots{display:flex;gap:4px;margin-top:9px}
.dots span{width:7px;height:7px;border-radius:50%;background:#fff}
.dots span:first-child{background:var(--orange)}

.features{position:absolute;top:268px;left:0;width:847px;height:268px;background:#fff;border-bottom:1px solid var(--line)}
.feature-row{position:absolute;left:127px;top:44px;width:593px;display:flex;justify-content:space-between}
.feature{width:170px;text-align:center}
.feature svg{width:30px;height:30px;display:block;margin:0 auto}
.feature h3{font-size:12px;font-weight:600;color:#555;margin-top:8px}
.feature p{font-size:6.5px;line-height:1.6;color:var(--muted);margin-top:6px}
.btn{display:inline-block;margin-top:10px;font-size:6px;font-weight:700;color:#fff;padding:4px 12px;border-radius:2px}
.btn-orange{background:var(--orange)}
.btn-blue{background:var(--blue)}
.btn-green{background:var(--green)}

.about{position:absolute;top:565px;left:0;width:847px;height:255px;background:linear-gradient(90deg,var(--cyan) 0%,var(--cyan-light) 100%)}
.about-photo{position:absolute;left:470px;top:-20px;width:280px;height:275px;background:linear-gradient(160deg,#cfeaf4 0%,#9fc9d8 55%,#5c8aa0 100%)}
.about-copy{position:absolute;left:127px;top:60px;width:320px;color:#fff}
.about-copy h2{font-size:16px;font-weight:600}
.about-copy p{font-size:6.5px;line-height:1.6;margin-top:6px;color:#eafaff}

.columns{position:absolute;top:833px;left:127px;width:593px;display:flex;justify-content:space-between}
.column{width:175px}
.column-photo{height:82px;background:linear-gradient(135deg,#d7e6ef,#9bb7c8)}
.column h3{font-size:12px;font-weight:600;color:var(--blue);margin-top:10px}
.column p{font-size:6.5px;line-height:1.6;color:var(--muted);margin-top:5px}

.site-footer{position:absolute;top:1130px;left:0;width:847px;height:70px;background:var(--footer);border-top:1px solid var(--line)}
.footer-links{position:absolute;left:127px;top:22px;font-size:7px;font-weight:600;color:#555;letter-spacing:.3px}
.copyright{position:absolute;left:127px;top:36px;font-size:6px;color:var(--muted)}
.social{position:absolute;right:127px;top:21px;display:flex;gap:4px}
.social span{width:10px;height:10px;border-radius:50%;background:var(--blue)}
</style>
</head>
<body>

<header class="site-header">
  <div class="brand"><span class="brand-mark"></span><span class="brand-name">Brightwater</span></div>
  <div class="lang">
    <span class="lang-flag"></span>English
    <svg viewBox="0 0 6 4"><path d="M0 0h6L3 4z" fill="#888"/></svg>
  </div>
</header>

<nav class="main-nav">
  <ul>
    <li>HOME</li><li>ABOUT US</li><li>TOURS</li><li>SERVICES</li><li>TRAVEL</li><li>CONTACT US</li>
  </ul>
</nav>

<section class="hero">
  <div class="hero-photo" role="img" aria-label="Smiling student with backpack holding a map in front of ancient standing stones"></div>
  <div class="hero-copy">
    <p class="hero-kicker">Donec dictum lectus non</p>
    <h1 class="hero-title">Australian Culture</h1>
    <p class="hero-text">Lorem ipsum dolor sit amet, consectetur adipiscing elit. Integer nec odio praesent libero sed cursus ante dapibus diam.</p>
    <div class="dots"><span></span><span></span><span></span><span></span></div>
  </div>
</section>

<section class="features">
  <div class="feature-row">
    <div class="feature">
      <svg viewBox="0 0 30 30"><path d="M27 4c-1-1-3 0-4 1l-5 5-11-3-2 2 9 5-4 5-4-1-1 1 4 3 3 4 1-1-1-4 5-4 5 9 2-2-3-11 5-5c1-1 2-3 1-4z" fill="var(--orange)"/></svg>
      <h3>Educational Tours</h3>
      <p>Lorem ipsum dolor sit amet consectetur adipiscing elit sed do eiusmod tempor incididunt ut labore et dolore magna.</p>
      <span class="btn btn-orange">READ MORE</span>
    </div>
    <div class="feature">
      <svg viewBox="0 0 30 30"><path d="M15 3C8 3 3 8 3 14h24c0-6-5-11-12-11z" fill="var(--blue)"/><path d="M15 14v10a2 2 0 0 1-4 0" stroke="var(--blue)" stroke-width="2" fill="none"/></svg>
      <h3>Travel Insurance</h3>
      <p>Lorem ipsum dolor sit amet consectetur adipiscing elit sed do eiusmod tempor incididunt ut labore et dolore magna.</p>
      <span class="btn btn-blue">READ MORE</span>
    </div>
    <div class="feature">
      <svg viewBox="0 0 30 30"><circle cx="15" cy="15" r="11" fill="none" stroke="var(--green)" stroke-width="6"/><circle cx="15" cy="15" r="11" fill="none" stroke="#fff" stroke-width="6" stroke-dasharray="5 12.3" stroke-dashoffset="2.5"/></svg>
      <h3>Safety &amp; Security</h3>
      <p>Lorem ipsum dolor sit amet consectetur adipiscing elit sed do eiusmod tempor incididunt ut labore et dolore magna.</p>
      <span class="btn btn-green">READ MORE</span>
    </div>
  </div>
</section>

<section class="about">
  <div class="about-photo" role="img" aria-label="Smiling student in glasses with a backpack"></div>
  <div class="about-copy">
    <h2>About Brightwater Learning Trips</h2>
    <p>Lorem ipsum dolor sit amet, consectetur adipiscing elit. Nullam sagittis dictum lacus, sed vehicula nisl porttitor at. Vivamus ut erat eu arcu pulvinar hendrerit vel id ligula.</p>
    <p>Curabitur blandit tempus porttitor. Donec ullamcorper nulla non metus auctor fringilla. Maecenas faucibus mollis interdum, sed posuere consectetur est at lobortis.</p>
    <p>Aenean lacinia bibendum nulla sed consectetur cras mattis consectetur purus.</p>
    <span class="btn btn-orange">READ MORE</span>
  </div>
</section>

<section class="columns">
  <article class="column">
    <div class="column-photo" role="img" aria-label="Group of smiling students"></div>
    <h3>Why Choose Us</h3>
    <p>Lorem ipsum dolor sit amet, consectetur adipiscing elit. Sed posuere consectetur est at lobortis, donec sed odio dui.</p>
  </article>
  <article class="column">
    <div class="column-photo" role="img" aria-label="Students gathered together on a tour"></div>
    <h3>Featured Tour</h3>
    <p>Lorem ipsum dolor sit amet, consectetur adipiscing elit. Sed posuere consectetur est at lobortis, donec sed odio dui.</p>
  </article>
  <article class="column">
    <div class="column-photo" role="img" aria-label="Student with books at school"></div>
    <h3>Our Education &amp; Culture</h3>
    <p>Lorem ipsum dolor sit amet, consectetur adipiscing elit. Sed posuere consectetur est at lobortis, donec sed odio dui.</p>
  </article>
</section>

<footer class="site-footer">
  <p class="footer-links">HOME &nbsp;|&nbsp; ABOUT US &nbsp;|&nbsp; SERVICES &nbsp;|&nbsp; TOUR &nbsp;|&nbsp; TRAVEL &nbsp;|&nbsp; CONTACT</p>
  <p class="copyright">© 2015 Brightwater Learning Trips. All rights reserved.</p>
  <div class="social"><span></span><span></span><span></span><span></span></div>
</footer>

</body>
</html>
```